Business cards for our company

We are a new online eLearning company. We create training for organizations that need to comply with governmental regulations. Our courses are built around the concept of an online show so our course has a media player / control bar across the bottom of all courses. We think this is an important element to work into the design. We have a simple mock up which we don't want anyone to just follow but just to give some idea of how the control bar could be used in the design but we are open to anything creative. If you choose to use the control bar, it doesn't have to be used literally. You can add/move/change buttons to suite your design concept. I have most of these files as PSD files so if you, need those just ask and I will post. The font in the course is Open Sans.
Also attached are the logo design and specs.

Target Market(s)

US corporations. Buyers are Senior HR executives, Chief Compiance Officer and General Counsels

Industry/Entity Type

Business

Contact Information for Business Card

Standard size cards. If it helps make the design more impactful, we'll do raised lettering

Font styles to use
Other font styles liked:
• Open Sans

Requirements
Must have
• must use our icon and logo using the supplied standards. needs to include our tag line as shown on the Word document (open to suggestions there as well). Should visually communicate that we are a next-generation eLearning company and not creating the same-old powerpoint looking, click next, click next type of training.

```html
<!DOCTYPE html>
<html lang="en">
<head>
<meta charset="utf-8">
<title>Veralon Business Card</title>
<link rel="stylesheet" href="https://fonts.googleapis.com/css2?family=Open+Sans:wght@400;600&display=swap">
<style>
  :root {
    --stage: #2b2b2b;
    --card-white: #f7f7f7;
    --card-black: #050505;
    --brand-blue: #1a9ad8;
    --brand-navy: #1b5fa8;
    --band-mid: #1283c6;
    --text-white: #f2f2f2;
  }
  * { margin: 0; padding: 0; box-sizing: border-box; }
  html, body {
    width: 1200px; height: 997px; overflow: hidden;
    background: var(--stage);
    font-family: "Open Sans", Arial, sans-serif;
  }
  .card {
    position: absolute; left: 150px; top: 241px;
    width: 900px; height: 514px;
    border-radius: 28px; overflow: hidden;
    background: var(--card-white);
  }
  .card-waves { position: absolute; inset: 0; width: 900px; height: 514px; }
  .brand {
    position: absolute; left: 0; right: 0; top: 44px;
    display: flex; flex-direction: column; align-items: center; gap: 12px;
  }
  .brand-square {
    width: 84px; height: 84px; border-radius: 14px;
    background: var(--brand-blue);
  }
  .brand-name {
    font-size: 62px; font-weight: 600; letter-spacing: 4px;
    color: var(--brand-navy); line-height: 1;
  }
  .contact {
    position: absolute; left: 42px; top: 345px;
    color: var(--text-white);
  }
  .contact-name {
    font-size: 22px; color: var(--brand-blue); letter-spacing: 0.5px; line-height: 1.2;
  }
  .contact-title { font-size: 16px; margin-bottom: 10px; }
  .contact-line {
    display: flex; align-items: center; gap: 10px;
    font-size: 17px; line-height: 27px;
  }
  .contact-line svg { width: 16px; height: 16px; fill: var(--brand-blue); }
  .web {
    position: absolute; right: 40px; top: 292px;
    font-size: 18px; letter-spacing: 1.5px; color: var(--brand-blue);
  }
</style>
</head>
<body>
  <div class="card">
    <svg class="card-waves" viewBox="0 0 900 514" aria-hidden="true">
      <path fill="var(--brand-blue)" d="M0,286 C200,288 380,344 560,310 C720,280 820,200 900,150 L900,514 L0,514 Z"/>
      <path fill="var(--brand-navy)" d="M0,292 C210,296 390,352 570,320 C730,292 830,218 900,176 L900,514 L0,514 Z"/>
      <path fill="var(--band-mid)" d="M0,298 C220,304 400,360 580,330 C740,302 840,236 900,200 L900,514 L0,514 Z"/>
      <path fill="var(--card-black)" d="M0,304 C230,312 410,368 590,340 C750,312 850,254 900,222 L900,514 L0,514 Z"/>
    </svg>

    <div class="brand">
      <div class="brand-square"></div>
      <div class="brand-name">VERALON</div>
    </div>

    <div class="web">www.Veralon.com</div>

    <div class="contact">
      <div class="contact-name">DANA WHITFIELD</div>
      <div class="contact-title">CEO</div>
      <div class="contact-line">
        <svg viewBox="0 0 16 16"><path d="M3 1h3l1.5 4-2 1.3a9 9 0 0 0 4.2 4.2L11 8.5l4 1.5v3a2 2 0 0 1-2 2A13 13 0 0 1 1 3a2 2 0 0 1 2-2z"/></svg>
        <span>212-555-0147</span>
      </div>
      <div class="contact-line">
        <svg viewBox="0 0 16 16"><path d="M4 0h8a1 1 0 0 1 1 1v14a1 1 0 0 1-1 1H4a1 1 0 0 1-1-1V1a1 1 0 0 1 1-1zm1 2v10h6V2zm3 11a1 1 0 1 0 0 2 1 1 0 0 0 0-2z"/></svg>
        <span>212-555-0183</span>
      </div>
      <div class="contact-line">
        <svg viewBox="0 0 16 16"><path d="M1 3h14v10H1zm1.5 1.2L8 8.6l5.5-4.4z"/></svg>
        <span>Dana.Whitfield@Veralon.com</span>
      </div>
    </div>
  </div>
</body>
</html>
```